Legal Campaign

A courier compavny that offer Legal services like filing/recording Court documents.
Updates

These info must be on card: Can We Help With Your Legal Services? Need Your Court documents quickly filed? .Filing/Recording in Erie, Niagara & Monroe County .Pick-up within 15-30 minutes of call .Medical records pick-up & delivery .Court-Authorized Process Servers .$9.00 Buffalo to Buffalo .Volume Discounts Call Drew Halvorn@716-555-0143 The address must be 48 Tillman Ave., Buffalo NY 14209

Please add the following info: 1.Post Office Pickup/Deliveries 2. Drewhalvorn@qrtlane.com

Target Market(s)

Law firms & legal community.

Industry/Entity Type

Court

Requirements
Must have
• RoutaSwift logo must be on card. Please visit the website@qrtlane.com to check out the logo. Thanks

```html
<!DOCTYPE html>
<html lang="en">
<head>
<meta charset="utf-8">
<title>RoutaSwift Legal Campaign Postcard</title>
<link rel="stylesheet" href="https://fonts.googleapis.com/css2?family=Open+Sans:wght@400;600;700&display=swap">
<style>
  :root {
    --stage: #666666;
    --card: #ffffff;
    --navy: #0c3f7c;
    --navy-deep: #072a57;
    --orange: #f07f1e;
    --sky: #1e9ad6;
    --sky-text: #3ea6e4;
    --charcoal: #3a3a3c;
    --rule: #b9b9b9;
    --white: #ffffff;
  }
  * { box-sizing: border-box; margin: 0; padding: 0; }
  html, body { width: 802px; height: 1200px; overflow: hidden; }
  body {
    background: var(--stage);
    font-family: "Open Sans", Arial, sans-serif;
    position: relative;
    color: var(--white);
  }
  .abs { position: absolute; }

  /* Front */
  .front { left: 52px; top: 54px; width: 698px; height: 537px; background: var(--card); overflow: hidden; }
  .front-photo {
    left: 0; top: 0; width: 698px; height: 371px;
    background: linear-gradient(100deg, #2c4466 0%, #5a6f8c 30%, #d9dde2 55%, #eef0f2 75%, #c9c2b5 100%);
  }
  .headline-panel {
    left: 0; top: 0; width: 320px; height: 318px;
    background: rgba(10, 50, 100, 0.72);
  }
  .logo-box {
    left: 38px; top: 0; width: 176px; height: 98px;
    background: var(--white);
    display: flex; align-items: center; justify-content: center;
  }
  .logo-name { color: var(--navy); font-weight: 700; font-size: 24px; letter-spacing: -0.3px; }
  .headline { left: 38px; top: 118px; line-height: 36px; }
  .headline p { font-size: 27px; font-weight: 400; }
  .headline b { font-weight: 700; }
  .headline .gap { margin-top: 17px; }
  .service-band {
    left: 0; top: 371px; width: 698px; height: 140px;
    background: linear-gradient(180deg, var(--navy) 0%, var(--navy-deep) 100%);
  }
  .service-list { list-style: none; top: 21px; font-size: 14px; line-height: 23px; }
  .service-list li { position: relative; padding-left: 12px; }
  .service-list li::before {
    content: ""; position: absolute; left: 0; top: 8px;
    width: 6px; height: 6px; background: var(--orange);
  }
  .service-list b { font-weight: 700; }
  .service-list .indent { padding-left: 16px; }
  .service-list .indent::before { display: none; }
  .list-left { left: 46px; }
  .list-right { left: 386px; }
  .service-list .discount { color: var(--orange); font-weight: 700; font-size: 21px; line-height: 26px; }
  .service-list .discount::before { top: 11px; }
  .url-band {
    left: 0; top: 511px; width: 698px; height: 26px;
    background: var(--orange);
    text-align: center; font-size: 13px; font-weight: 700; letter-spacing: 1.5px; line-height: 26px;
  }

  /* Back */
  .back { left: 52px; top: 613px; width: 698px; height: 537px; background: var(--card); overflow: hidden; }
  .back-accent { left: 0; top: 0; width: 340px; height: 5px; background: var(--orange); }
  .back-photo {
    left: 0; top: 5px; width: 340px; height: 248px;
    background: linear-gradient(110deg, #2b3340 0%, #8a939e 35%, #e6e8ea 60%, #cfc8ba 100%);
  }
  .callout {
    left: 161px; top: 158px; width: 102px; height: 102px; border-radius: 50%;
    background: var(--sky);
    display: flex; align-items: center; justify-content: center; text-align: center;
    font-size: 18px; line-height: 23px;
  }
  .contact-panel { left: 0; top: 253px; width: 340px; height: 130px; background: var(--charcoal); }
  .contact-icon { left: 44px; width: 38px; height: 38px; }
  .contact-label { left: 101px; color: var(--sky-text); font-size: 19px; }
  .contact-value { left: 101px; font-size: 21px; }
  .contact-value.email { font-size: 16px; }
  .address-band {
    left: 0; top: 385px; width: 340px; height: 62px;
    background: linear-gradient(180deg, var(--navy) 0%, var(--navy-deep) 100%);
    text-align: center; font-size: 15px; line-height: 20px; padding-top: 12px;
  }
  .stamp-box { left: 544px; top: 35px; width: 110px; height: 130px; border: 1px solid var(--rule); }
  .address-line { left: 373px; width: 281px; border-top: 1px dotted var(--rule); }
</style>
</head>
<body>

<section class="front abs">
  <div class="front-photo abs" role="img" aria-label="Photo of a lawyer's hands at a desk with documents, a pen and a bronze statue of Lady Justice, with a running courier carrying a parcel"></div>
  <div class="headline-panel abs"></div>
  <div class="logo-box abs"><span class="logo-name">RoutaSwift</span></div>
  <div class="headline abs">
    <p>Can We <b>Help</b> With</p>
    <p><b>Your Legal Services</b>?</p>
    <p class="gap">Need Your</p>
    <p><b>Court documents</b></p>
    <p><b>quickly filed</b>?</p>
  </div>
  <div class="service-band abs">
    <ul class="service-list list-left abs">
      <li><b>Post Office Pickup/Deliveries.</b></li>
      <li><b>Filing/Recording</b> in Erie,</li>
      <li class="indent">Niagara &amp; Monroe County.</li>
      <li><b>Pick-up</b> within 15-30 minutes of call.</li>
    </ul>
    <ul class="service-list list-right abs">
      <li><b>Medical records</b> pick-up &amp; delivery.</li>
      <li><b>Court-Authorized Process Servers</b>.</li>
      <li>$9.00 Buffalo to Buffalo.</li>
      <li class="discount">Volume Discounts</li>
    </ul>
  </div>
  <div class="url-band abs">www.qrtlane.com</div>
</section>

<section class="back abs">
  <div class="back-accent abs"></div>
  <div class="back-photo abs" role="img" aria-label="Photo of a lawyer stamping a document beside a bronze Lady Justice statue"></div>
  <div class="callout abs">How to<br>deliver<br>on time?</div>

  <div class="contact-panel abs">
    <svg class="contact-icon abs" style="top:15px" viewBox="0 0 38 38" aria-hidden="true">
      <circle cx="19" cy="19" r="18" fill="#5d8fc0" stroke="#d7e6f3" stroke-width="2"/>
      <path d="M11 16c0-3 4-4 8-4s8 1 8 4v2h-4v-2h-8v2h-4z M13 20h12l2 7H11z" fill="#ffffff"/>
      <circle cx="19" cy="23" r="2" fill="#5d8fc0"/>
    </svg>
    <div class="contact-label abs" style="top:14px">Call Drew Halvorn@</div>
    <div class="contact-value abs" style="top:36px">716-555-0143</div>

    <svg class="contact-icon abs" style="top:78px" viewBox="0 0 38 38" aria-hidden="true">
      <circle cx="19" cy="19" r="18" fill="#5d8fc0" stroke="#d7e6f3" stroke-width="2"/>
      <rect x="10" y="13" width="18" height="12" fill="#ffffff"/>
      <path d="M10 13l9 7 9-7" fill="none" stroke="#5d8fc0" stroke-width="1.5"/>
    </svg>
    <div class="contact-label abs" style="top:74px">or write to:</div>
    <div class="contact-value email abs" style="top:96px">Drewhalvorn@qrtlane.com</div>
  </div>

  <div class="address-band abs">
    48 Tillman Ave., Buffalo NY 14209<br>www.qrtlane.com
  </div>

  <div class="stamp-box abs"></div>
  <div class="address-line abs" style="top:224px"></div>
  <div class="address-line abs" style="top:252px"></div>
  <div class="address-line abs" style="top:280px"></div>
  <div class="address-line abs" style="top:308px"></div>
  <div class="address-line abs" style="top:336px"></div>
  <div class="address-line abs" style="top:364px"></div>
</section>

</body>
</html>
```